Powerpoint template for Waste Management company

We need a professional look and feeling for our powerpoint presentation templates. Company is based on three pillars: componsting solutions, collecting solutions and recycling solutions. We area looking for ppt templates for the front page, regular slide and at leat one slide template specific for each pillar (total 5-6 slide templates). I have attached the logo.

Target Market(s)

Companies, Goverment, Municipalities

Industry/Entity Type

Waste Management

Font styles to use
Serif

```html
<!DOCTYPE html>
<html lang="en">
<head>
<meta charset="utf-8">
<title>Greenloop Waste – Slide Templates</title>
<link href="https://fonts.googleapis.com/css2?family=Raleway:wght@400;600;700&display=swap" rel="stylesheet">
<style>
  :root{
    --green:#3bb54a;
    --green-soft:#8fd69a;
    --orange:#f15a24;
    --orange-soft:#f8a27f;
    --blue:#0b6fbb;
    --blue-soft:#7fb4e0;
    --grey:#8c8c8c;
    --title:#6b6b6b;
    --text:#7a7a7a;
    --note:#8a8a8a;
    --panel:#f1f1f1;
    --page:#ffffff;
  }
  *{box-sizing:border-box;margin:0;padding:0}
  html,body{width:1200px;height:4091px;overflow:hidden;background:var(--page)}
  body{position:relative;font-family:"Raleway",sans-serif;color:var(--text)}

  .slide{position:absolute;left:109px;width:982px;height:552px;background:#fff;overflow:hidden;box-shadow:0 2px 6px rgba(0,0,0,.18)}
  .slide > svg.bg{position:absolute;inset:0;width:100%;height:100%}

  /* title slides */
  .band{position:absolute;left:0;width:100%}
  .band.top{top:0;height:120px}
  .band.bottom{bottom:0;height:130px}
  .band.tricolour{background:linear-gradient(90deg,var(--green) 0 30%,var(--orange) 30% 68%,var(--blue) 68%)}
  .cover-title{position:absolute;left:41px;top:190px;font-size:58px;line-height:62px;font-weight:700;color:var(--title);letter-spacing:-.5px}
  .cover-sub{position:absolute;left:43px;top:322px;font-size:15px;color:var(--text)}
  .cover-sub b{font-weight:600}
  .brand-panel{position:absolute;left:622px;top:186px;width:311px;height:174px;background:var(--panel);border-top:9px solid var(--green);border-bottom:9px solid var(--green);display:flex;align-items:center;justify-content:center;gap:12px}
  .brand-panel .mark{width:26px;height:26px;background:var(--green)}
  .brand-panel .name{font-size:24px;font-weight:700;color:#444}

  /* content slides */
  .edge{position:absolute;left:0;top:100px;width:8px;bottom:0}
  .head{position:absolute;left:30px;top:18px}
  .head h2{font-size:38px;font-weight:700;color:var(--title);line-height:44px}
  .head p{font-size:15px;color:var(--text);margin-left:2px}
  .footer{position:absolute;left:64px;bottom:10px;font-size:10px;color:#999}
  .pageno{position:absolute;right:16px;bottom:10px;font-size:11px;color:#fff}
  .art{position:absolute;border-radius:14px}

  .stat{position:absolute;left:260px;width:380px;height:96px}
  .stat .label{position:absolute;left:60px;top:0;font-size:15px;color:#888}
  .stat .rule{position:absolute;left:0;top:22px;width:380px;height:1px;background:#9a9a9a}
  .stat .value{position:absolute;left:0;top:34px;font-size:44px;line-height:50px;font-weight:700}
  .stat .note{position:absolute;left:160px;top:36px;width:170px;font-size:10.5px;line-height:15px;color:var(--note)}
  .chart{position:absolute;left:660px;top:130px;width:220px;height:180px}
  .chart-note{position:absolute;left:672px;top:330px;width:170px;font-size:10.5px;line-height:16px;color:var(--note)}

  .truck-col{position:absolute;top:130px;width:210px}
  .truck-col .art{position:relative;width:200px;height:120px}
  .truck-col .kind{margin-top:30px;font-size:15px;color:#888}
  .truck-col .amount{font-size:38px;line-height:44px}
  .truck-col .desc{font-size:13px;line-height:19px;color:var(--note);margin-top:6px;width:190px}

  .step{position:absolute;left:82px;width:286px}
  .step .bar{height:24px;color:#fff;font-size:13px;padding:4px 10px}
  .step ul{list-style:none;margin-top:8px}
  .step li{font-size:11px;line-height:19px;color:#888;padding-left:22px;position:relative}
  .step li::before{content:"";position:absolute;left:10px;top:8px;width:4px;height:4px;border-radius:50%;background:var(--dot)}
</style>
</head>
<body>

<!-- Cover -->
<section class="slide" style="top:0">
  <div class="band top tricolour" style="height:92px"></div>
  <div class="band bottom tricolour" style="height:143px"></div>
  <h1 class="cover-title">Business<br>Presentation</h1>
  <p class="cover-sub">Your Subtitle Goes Here</p>
  <div class="brand-panel"><span class="mark"></span><span class="name">Greenloop Waste</span></div>
</section>

<!-- Composting title -->
<section class="slide" style="top:587px">
  <div class="band top" style="background:var(--green)"></div>
  <div class="band bottom" style="background:var(--green)"></div>
  <h1 class="cover-title">Componsting<br>Solutions</h1>
  <p class="cover-sub" style="color:var(--green)">Your <b>Subtitle Goes Here</b></p>
  <div class="brand-panel"><span class="mark"></span><span class="name">Greenloop Waste</span></div>
</section>

<!-- Composting content -->
<section class="slide" style="top:1174px">
  <svg class="bg" viewBox="0 0 982 552" preserveAspectRatio="none">
    <polygon points="930,200 982,150 982,552 820,552" fill="var(--green)"/>
  </svg>
  <div class="edge" style="background:var(--green)"></div>
  <div class="head"><h2>Componsting Solutions</h2><p>Your Subtitle Goes Here</p></div>
  <div class="art" role="img" aria-label="Leaf illustration divided into blue, orange and green sections"
       style="left:34px;top:115px;width:200px;height:360px;background:linear-gradient(180deg,var(--blue-soft),var(--orange-soft) 50%,var(--green-soft))"></div>

  <div class="stat" style="top:112px"><div class="label">Insert Text</div><div class="rule"></div><div class="value" style="color:var(--blue)">43%</div><div class="note">All files and graphics on the template is editable because is all based on vector</div></div>
  <div class="stat" style="top:216px"><div class="label" style="left:80px">Insert Text</div><div class="rule"></div><div class="value" style="color:var(--green)">32%</div><div class="note">All files and graphics on the template is editable because is all based on vector</div></div>
  <div class="stat" style="top:320px"><div class="label" style="left:100px">Insert Text</div><div class="rule"></div><div class="value" style="color:var(--orange)">27%</div><div class="note">All files and graphics on the template is editable because is all based on vector</div></div>

  <svg class="chart" viewBox="0 0 220 180">
    <g font-family="Raleway, sans-serif" font-size="9" fill="#888" text-anchor="end">
      <text x="18" y="150">0</text><text x="18" y="126">0.5</text><text x="18" y="102">1</text>
      <text x="18" y="78">1.5</text><text x="18" y="54">2</text><text x="18" y="30">2.5</text><text x="18" y="6">3</text>
    </g>
    <line x1="26" y1="147" x2="210" y2="147" stroke="#ccc"/>
    <rect x="50" y="50" width="34" height="97" fill="var(--green)"/>
    <rect x="96" y="30" width="34" height="117" fill="var(--orange)"/>
    <rect x="142" y="20" width="34" height="127" fill="var(--blue)"/>
    <text x="113" y="165" font-family="Raleway, sans-serif" font-size="9" fill="#888" text-anchor="middle">Category 1</text>
  </svg>
  <p class="chart-note">For every six requests we receive, three turn into site visits. Suitable for all categories, business and personal presentations, easy to edit and ready for your own numbers and words.</p>
  <p class="footer">© 2017 Greenloop Waste. All rights reserved.</p>
  <p class="pageno">3</p>
</section>

<!-- Collecting title -->
<section class="slide" style="top:1761px">
  <div class="band top" style="background:var(--orange)"></div>
  <div class="band bottom" style="background:var(--orange)"></div>
  <h1 class="cover-title">Collecting<br>Solutions</h1>
  <p class="cover-sub" style="color:var(--orange)">Your <b>Subtitle Goes Here</b></p>
  <div class="brand-panel"><span class="mark"></span><span class="name">Greenloop Waste</span></div>
</section>

<!-- Collecting content -->
<section class="slide" style="top:2348px">
  <svg class="bg" viewBox="0 0 982 552" preserveAspectRatio="none">
    <polygon points="935,240 982,190 982,552 860,552" fill="var(--orange)"/>
  </svg>
  <div class="edge" style="background:var(--orange)"></div>
  <div class="head"><h2>Collecting Solutions</h2><p>Your Subtitle Goes Here</p></div>

  <div class="truck-col" style="left:48px">
    <div class="art" role="img" aria-label="Grey dump truck carrying an orange load" style="background:linear-gradient(180deg,var(--orange-soft),#c9c9c9)"></div>
    <p class="kind">Waste</p><p class="amount" style="color:var(--orange)">$2M</p>
    <p class="desc">Click the shape on truck, ungroup it and recolor a fill with your own.</p>
  </div>
  <div class="truck-col" style="left:355px">
    <div class="art" role="img" aria-label="Grey dump truck carrying a green load" style="background:linear-gradient(180deg,var(--green-soft),#c9c9c9)"></div>
    <p class="kind">waste</p><p class="amount" style="color:var(--green)">$5M</p>
    <p class="desc">Click the shape on truck, ungroup it and recolor a fill with your own.</p>
  </div>
  <div class="truck-col" style="left:662px">
    <div class="art" role="img" aria-label="Grey dump truck carrying a blue load" style="background:linear-gradient(180deg,var(--blue-soft),#c9c9c9)"></div>
    <p class="kind">waste</p><p class="amount" style="color:var(--blue)">$3,5M</p>
    <p class="desc">Click the shape on truck, ungroup it and recolor a fill with your own.</p>
  </div>
  <p class="footer">© 2017 Greenloop Waste. All rights reserved.</p>
  <p class="pageno">5</p>
</section>

<!-- Recycling title -->
<section class="slide" style="top:2935px">
  <div class="band top" style="background:var(--blue)"></div>
  <div class="band bottom" style="background:var(--blue)"></div>
  <h1 class="cover-title">Recycling<br>Solutions</h1>
  <p class="cover-sub" style="color:var(--blue)">Your <b>Subtitle Goes Here</b></p>
  <div class="brand-panel"><span class="mark"></span><span class="name">Greenloop Waste</span></div>
</section>

<!-- Recycling content -->
<section class="slide" style="top:3522px">
  <svg class="bg" viewBox="0 0 982 552" preserveAspectRatio="none">
    <polygon points="935,240 982,190 982,552 860,552" fill="var(--blue)"/>
  </svg>
  <div class="edge" style="background:var(--blue)"></div>
  <div class="head"><h2>Recycling Solutions</h2><p>Your Subtitle Goes Here</p></div>

  <div class="step" style="top:112px;--dot:var(--blue)">
    <div class="bar" style="background:var(--blue)">Input</div>
    <ul><li>Donec eu dui eget nisl rhoncus volutpat</li><li>Quisque et magna faucibus vestibulum</li><li>Donec convallis mauris rutrum finibus</li></ul>
  </div>
  <div class="step" style="top:245px;--dot:var(--orange)">
    <div class="bar" style="background:var(--orange)">Process</div>
    <ul><li>Donec eu dui eget nisl rhoncus volutpat</li><li>Quisque et magna faucibus vestibulum</li></ul>
  </div>
  <div class="step" style="top:350px;--dot:var(--green)">
    <div class="bar" style="background:var(--green)">Output</div>
    <ul><li>Donec eu dui eget nisl rhoncus volutpat</li><li>Quisque et magna faucibus vestibulum</li><li>Donec convallis mauris rutrum finibus</li></ul>
  </div>

  <div class="art" role="img" aria-label="Recycling cycle graphic with input, process and output arrows in blue, orange and green"
       style="left:500px;top:110px;width:320px;height:330px;background:linear-gradient(135deg,var(--blue-soft),var(--orange-soft) 55%,var(--green-soft))"></div>
  <p class="footer">© 2017 Greenloop Waste. All rights reserved.</p>
  <p class="pageno">7</p>
</section>

</body>
</html>
```